Local business providing residential house cleaning services

We need a business card design that is "cute" or "cartoonish" while still maintaining a professional appeal. Tidy Lark Cleaners is the name. We would like to use a "pin up girl" or maid next to the name with a broom or vacuum cleaner. We want the look to have a 50's American look to it. We are not sure if we want the pin up girl in a maid outfit or with a broom or vacuum cleaner but we hope some of you will be able to take these ideas and be creative. If you have any questions at all please don't hesitate to message me so that we can get the best design possible. Thank you very much and I look forward to seeing some designs! Mona Pritchett

Target Market(s)

Upper class Americans that are busy and have money and want to come home to a clean house.

Industry/Entity Type

Cleaning Service

Contact Information for Business Card

Pin up girl incorporated into the card is a must.

Font styles to use
Decorative
Script

Requirements
Must have
• Pin up girl
Nice to have
• A crown used on the Q possibly.

```html
<!DOCTYPE html>
<html lang="en">
<head>
<meta charset="utf-8">
<title>Tidy Lark Cleaners — Business Card</title>
<link rel="stylesheet" href="https://fonts.googleapis.com/css2?family=Tangerine:wght@700&family=Arimo&display=swap">
<style>
  :root {
    --backdrop: #737373;
    --card-light: #dce8f2;
    --card-mid: #a9cfe0;
    --card-teal: #86c8d3;
    --ink-teal: #2c5a66;
    --logo-white: #ffffff;
    --rule: #4f7a86;
    --art-haze: rgba(236, 242, 250, 0.95);
    --art-cream: rgba(238, 228, 205, 0.95);
    --art-skin: rgba(226, 190, 160, 0.85);
    --art-shadow: rgba(170, 150, 120, 0.35);
  }
  * { box-sizing: border-box; margin: 0; padding: 0; }
  html, body {
    width: 974px;
    height: 1200px;
    overflow: hidden;
    background: var(--backdrop);
  }
  .canvas {
    position: relative;
    width: 974px;
    height: 1200px;
  }
  .card {
    position: absolute;
    width: 844px;
    height: 460px;
    overflow: hidden;
    box-shadow: 0 2px 3px rgba(0,0,0,0.25);
  }
  .card--front {
    left: 57px;
    top: 117px;
    background: linear-gradient(100deg, var(--card-light) 0%, var(--card-mid) 45%, var(--card-teal) 100%);
  }
  .card--back {
    left: 62px;
    top: 636px;
    background: linear-gradient(100deg, var(--card-teal) 0%, var(--card-mid) 50%, var(--card-teal) 100%);
  }
  .pinup-art {
    position: absolute;
    left: 0;
    top: 0;
    width: 440px;
    height: 460px;
    background:
      radial-gradient(closest-side at 200px 200px, var(--art-cream) 0%, rgba(238,228,205,0.6) 45%, rgba(238,228,205,0) 100%),
      radial-gradient(closest-side at 195px 340px, var(--art-skin) 0%, rgba(226,190,160,0.35) 55%, rgba(226,190,160,0) 100%),
      radial-gradient(closest-side at 300px 380px, var(--art-shadow) 0%, rgba(170,150,120,0) 100%),
      radial-gradient(closest-side at 190px 240px, var(--art-haze) 0%, rgba(236,242,250,0.7) 60%, rgba(236,242,250,0) 100%);
  }
  .brand-name {
    position: absolute;
    left: 380px;
    top: 120px;
    width: 440px;
    text-align: center;
    font-family: "Tangerine", cursive;
    font-weight: 700;
    font-size: 96px;
    line-height: 0.95;
    color: var(--logo-white);
  }
  .contact {
    position: absolute;
    inset: 0;
    text-align: center;
  }
  .contact__name {
    position: absolute;
    left: 0;
    right: 0;
    top: 140px;
    font-family: "Tangerine", cursive;
    font-weight: 700;
    font-size: 80px;
    line-height: 1;
    color: var(--ink-teal);
    letter-spacing: 1px;
  }
  .contact__rule {
    position: absolute;
    left: 251px;
    top: 246px;
    width: 344px;
    height: 14px;
  }
  .contact__phone {
    position: absolute;
    left: 0;
    right: 0;
    top: 299px;
    font-family: "Arimo", Arial, sans-serif;
    font-size: 29px;
    color: var(--ink-teal);
    letter-spacing: 0.5px;
  }
</style>
</head>
<body>
  <main class="canvas">
    <section class="card card--front">
      <div class="pinup-art" role="img" aria-label="Illustration of a 1950s pin-up maid in a frilly apron and green heels, holding a broom"></div>
      <h1 class="brand-name">Tidy Lark<br>Cleaners</h1>
    </section>

    <section class="card card--back">
      <div class="contact">
        <p class="contact__name">Mona Pritchett</p>
        <svg class="contact__rule" viewBox="0 0 344 14" aria-hidden="true">
          <line x1="0" y1="7" x2="344" y2="7" stroke="var(--rule)" stroke-width="1.5"/>
          <rect x="166" y="1" width="12" height="12" transform="rotate(45 172 7)" fill="none" stroke="var(--rule)" stroke-width="1.5"/>
        </svg>
        <p class="contact__phone">501-555-0148</p>
      </div>
    </section>
  </main>
</body>
</html>
```